Toward Bright Morrow (TWBM) Business Card - company with a mission

Note* The file attached... orange with "Toward Bright MORROW" (in CAPS) is our logo. I am also open to having the text "toward bright morrow" OUTSIDE the orange round logo for business card (so yes, you may take the text out).

The info: (the following info are separate. So either you can use Martin or Helena for now, but that will be 2 separate cards, not together in one card. Thanks!!

Martin K Pardo
202.555.0183
martin@towardbrightmorrow.example
Managing Partner

Helena R Voss
202.555.0147
helena@towardbrightmorrow.example
Managing Partner

Our website: www.towardbrightmorrow.example

TWBM LLC stands for Toward Bright Morrow (non profit arm is called dawn lift foundation)—our business is based out of New York City and has a non-profit arm where for every bar of soap you purchase, we donate a bar (don’t want any designs that limits us to only soap). Currently working with South Africa. We want the focus to be organic/natural soap with a mission.

Looking for a clean, fresh design.

Industry/Entity Type

Non-Profit

Requirements
Must have
• Clean, fresh, refreshing. Design should not be too busy.

```html
<!DOCTYPE html>
<html lang="en">
<head>
<meta charset="utf-8">
<title>Toward Bright Morrow – Business Card</title>
<link rel="stylesheet" href="https://fonts.googleapis.com/css2?family=Open+Sans:wght@400;600;700&display=swap">
<style>
  :root {
    --page-bg: #e7e9ec;
    --card-dark: #3d3d3d;
    --card-light: #ffffff;
    --ink: #2b2b2b;
    --ink-soft: #555555;
    --on-dark: #ffffff;
    --rule: #3a3a3a;
  }
  * { box-sizing: border-box; margin: 0; padding: 0; }
  html, body {
    width: 1200px; height: 1024px; overflow: hidden;
    background: var(--page-bg);
    font-family: "Open Sans", Arial, sans-serif;
  }
  .sheet {
    width: 1200px; height: 1024px;
    display: flex; flex-direction: column; align-items: center; justify-content: center;
    gap: 72px;
  }
  .card {
    position: relative;
    width: 700px; height: 400px;
    border-radius: 26px;
    box-shadow: 0 10px 28px rgba(0,0,0,.18);
  }
  .card--front { background: var(--card-dark); color: var(--on-dark); }
  .card--back { background: var(--card-light); color: var(--ink); }

  .brand { position: absolute; display: flex; align-items: center; gap: 22px; }
  .brand__mark { width: 118px; height: 118px; border-radius: 50%; flex: none; }
  .brand__name { font-size: 34px; font-weight: 400; letter-spacing: .3px; }
  .card--front .brand { left: 150px; top: 140px; }
  .card--front .brand__mark { background: var(--on-dark); }
  .card--back .brand { left: 60px; top: 44px; }
  .card--back .brand__mark { background: var(--card-dark); width: 110px; height: 110px; }
  .card--back .brand__name { color: var(--ink); }

  .website {
    position: absolute; right: 46px; bottom: 36px;
    font-size: 17px; letter-spacing: .4px; color: var(--on-dark);
  }

  .person { position: absolute; left: 60px; top: 186px; }
  .person__name { font-size: 25px; font-weight: 700; }
  .person__title {
    font-size: 15px; color: var(--ink-soft);
    padding-bottom: 8px; border-bottom: 1.5px solid var(--rule);
    width: 230px;
  }
  .contact {
    position: absolute; left: 60px; top: 290px;
    display: flex; align-items: center; gap: 18px;
    font-size: 16px; color: var(--ink);
  }
  .contact__item { display: flex; align-items: center; gap: 7px; }
  .contact__icon { width: 16px; height: 16px; }
  .address {
    position: absolute; left: 60px; top: 332px;
    font-size: 18px; letter-spacing: 1.2px; color: var(--ink);
  }
</style>
</head>
<body>
<main class="sheet">
  <section class="card card--front" aria-label="Card front">
    <div class="brand">
      <span class="brand__mark"></span>
      <span class="brand__name">towardbrightmorrow</span>
    </div>
    <p class="website">www.yourwebsite.com</p>
  </section>

  <section class="card card--back" aria-label="Card back">
    <div class="brand">
      <span class="brand__mark"></span>
      <span class="brand__name">towardbrightmorrow</span>
    </div>
    <div class="person">
      <h1 class="person__name">Martin K Pardo</h1>
      <p class="person__title">Managing Partner</p>
    </div>
    <div class="contact">
      <span class="contact__item">
        <svg class="contact__icon" viewBox="0 0 16 16" aria-hidden="true">
          <circle cx="8" cy="8" r="8" fill="#2b2b2b"/>
          <path d="M5.2 4.2l1.4 1.4-.8 1.1c.5 1.2 1.4 2.1 2.6 2.6l1.1-.8 1.4 1.4-.9 1.3C7.6 11 5 8.4 4.2 5.1z" fill="#fff"/>
        </svg>
        202.555.0183
      </span>
      <span class="contact__item">
        <svg class="contact__icon" viewBox="0 0 16 16" aria-hidden="true">
          <rect width="16" height="16" rx="2" fill="#2b2b2b"/>
          <rect x="3" y="4.5" width="10" height="7" fill="none" stroke="#fff" stroke-width="1.1"/>
          <path d="M3 4.8l5 4 5-4" fill="none" stroke="#fff" stroke-width="1.1"/>
        </svg>
        martin@towardbrightmorrow.example
      </span>
    </div>
    <p class="address">418 Linden 27 Harbor St, Kingsford, ON K9Z 4T7</p>
  </section>
</main>
</body>
</html>
```